Website Monitoring Business Needs a Single Page Website Design

I need a website design for a new web based service called TallyNest. This service checks to see if a website is up or down and how quickly or slowly it is responding. Users sign up for a small monthly fee and add one or more websites to monitor based on the plan they purchase. I prefer a single page design.

There will be 3 pricing plans to start with. A free plan and then 2 paid plans. The pricing plans should be included on the single page.

Here are four close competitors to what this product will offer:

https://www.vorbelix.com/
http://quellarind.com/
https://www.marbotrix.com/
https://www.dune58kq.com/

Target Market(s)

Website owners, bloggers

Industry/Entity Type

Business

Coding

Coded - Design and coding required

Number of Pages Required

1 page

Font styles to use
Sans Serif

Requirements
Must have
• Responsive design
Nice to have
• Parallax scrolling

```html
<!DOCTYPE html>
<html lang="en">
<head>
<meta charset="utf-8">
<title>TallyNest – Website Monitoring</title>
<link rel="stylesheet" href="https://fonts.googleapis.com/css2?family=PT+Sans:wght@400;700&display=swap">
<style>
:root{
  --blue:#0a4fa6;
  --blue-dark:#073a7c;
  --yellow:#f2dc0a;
  --ink:#222;
  --text:#333;
  --muted:#777;
  --light:#f0f0f0;
  --card:#e9e9e9;
  --dark:#1d1d1d;
  --dark-2:#2b2b2b;
  --white:#fff;
}
*{box-sizing:border-box;margin:0;padding:0}
html,body{width:1200px;height:3186px;overflow:hidden}
body{font-family:"PT Sans",Arial,sans-serif;color:var(--text);background:var(--white);position:relative}
.wrap{width:952px;margin:0 auto;position:relative}
svg{display:block}

/* header */
.site-header{height:77px;border-bottom:4px solid var(--blue);position:relative;background:var(--white)}
.brand{position:absolute;left:124px;top:8px;display:flex;flex-direction:column;align-items:flex-start}
.brand-mark{width:26px;height:26px;background:var(--yellow);margin-left:4px}
.brand-name{font-size:22px;font-weight:700;color:var(--ink);margin-top:4px}
.top-contact{position:absolute;right:124px;top:8px;display:flex;gap:26px;font-size:14px;color:var(--ink)}
.top-contact span{display:flex;align-items:center;gap:8px}
.top-contact i{width:14px;height:14px;background:var(--blue);border-radius:2px;display:inline-block}
.nav{position:absolute;right:124px;bottom:0;display:flex;align-items:flex-end}
.nav a{font-size:14px;color:var(--ink);text-decoration:none;padding:8px 11px;height:32px}
.nav a.active{background:var(--blue);color:var(--white)}
.nav .signup{background:var(--blue);color:var(--white);width:150px;text-align:center;margin-left:14px;border-radius:10px 0 0 0}
.nav .login{background:#2d2d2d;color:#ddd;width:150px;text-align:center;border-radius:0 10px 0 0}

/* hero */
.hero{height:506px;position:relative;border-bottom:6px solid var(--yellow)}
.hero-photo{position:absolute;inset:0;background:linear-gradient(160deg,#3b3b3b 0%,#6b6b6b 35%,#8e8e8e 55%,#3f3f3f 80%,#222 100%)}
.hero-box{position:absolute;left:261px;top:94px;width:682px;height:268px;background:rgba(40,40,40,.82);text-align:center;padding:32px 48px 0}
.hero-box::before{content:"";position:absolute;right:0;top:0;width:570px;height:100%;border-top:3px solid var(--yellow);border-right:3px solid var(--yellow);border-bottom:3px solid var(--yellow);pointer-events:none}
.hero-title{font-size:42px;font-weight:400;color:var(--white);line-height:1.1}
.hero-title strong{display:block;color:var(--yellow);font-weight:700}
.hero-text{font-size:11.5px;color:#e3e3e3;line-height:1.55;margin-top:14px}
.btn-row{display:flex;align-items:center;gap:6px}
.hero .btn-row{justify-content:center;margin-top:16px}
.btn-yellow{background:var(--yellow);color:var(--ink);font-size:14px;font-weight:700;padding:6px 28px;border-radius:3px}
.btn-icon{width:26px;height:26px;background:#333;border-radius:3px;border:1px solid #888;display:flex;align-items:center;justify-content:center}
.hero-notch{position:absolute;left:580px;bottom:-26px;width:40px;height:20px;background:var(--yellow);clip-path:polygon(0 0,100% 0,50% 100%);z-index:2}

/* welcome */
.welcome{height:215px;background:var(--light);text-align:center;padding-top:42px}
.section-title{font-size:30px;font-weight:400;color:var(--blue)}
.welcome p{font-size:13px;color:var(--text);line-height:1.5;width:930px;margin:14px auto 0}
.welcome p+p{margin-top:12px}

/* services */
.services{height:460px;position:relative;text-align:center;padding-top:36px}
.services-photo{position:absolute;inset:0;background:linear-gradient(180deg,#111 0%,#2a2a2a 50%,#1a1a1a 100%)}
.services .section-title{color:var(--yellow);position:relative}
.service-list{position:relative;display:flex;gap:13px;width:952px;margin:44px auto 0}
.service-card{width:228px;height:282px;background:var(--white);padding:18px 18px 0;position:relative;clip-path:polygon(0 0,100% 0,100% 92%,50% 100%,0 92%)}
.hex{width:54px;height:60px;background:var(--blue);clip-path:polygon(50% 0,100% 25%,100% 75%,50% 100%,0 75%,0 25%);margin:0 auto;display:flex;align-items:center;justify-content:center}
.service-card h3{font-size:17px;color:var(--blue);margin-top:14px}
.service-card p{font-size:12.5px;color:var(--text);line-height:1.35;margin-top:6px}
.card-plus{position:absolute;left:50%;bottom:34px;transform:translateX(-50%);display:flex;align-items:center;gap:4px}
.card-plus b{width:26px;height:1px;background:#aaa}
.card-plus i{width:14px;height:14px;background:var(--blue);color:var(--white);font-style:normal;font-size:12px;line-height:14px;border-radius:2px}
.dots{position:relative;display:flex;justify-content:center;gap:4px;margin-top:32px}
.dots i{width:7px;height:7px;border-radius:50%;border:1px solid var(--yellow)}
.dots i:first-child{background:var(--yellow)}

/* cta band */
.cta{height:118px;position:relative;color:var(--white)}
.cta svg.wave{position:absolute;left:0;top:-20px}
.cta-inner{position:absolute;left:152px;top:22px;width:920px;display:flex;align-items:center}
.cta h2{font-size:23px;color:var(--yellow);font-weight:700}
.cta-copy{width:420px}
.cta-copy p{font-size:11px;line-height:1.4;margin-top:4px}
.cta-arrow{width:40px;height:40px;border:2px solid var(--yellow);border-radius:50%;margin-left:96px;display:flex;align-items:center;justify-content:center}
.cta-contact{margin-left:50px;font-size:14px;line-height:2}
.cta-contact b{color:var(--yellow)}

/* how */
.how{height:482px;position:relative}
.how-copy{position:absolute;left:126px;top:32px;width:360px}
.how-copy h2{font-size:30px;font-weight:400;color:var(--blue)}
.how-copy p{font-size:12.5px;line-height:1.55;margin-top:22px}
.how-copy .btn-row{margin-top:22px}
.monitor{position:absolute;left:574px;top:44px;width:500px;height:360px;border-radius:8px;background:linear-gradient(180deg,#1b1b1b 0,#1b1b1b 78%,#d5d5d5 78%,#bcbcbc 100%)}
.how-rule{position:absolute;left:100px;right:100px;bottom:4px;height:10px;background:radial-gradient(ellipse at center,rgba(0,0,0,.18),rgba(0,0,0,0) 70%)}

/* pricing */
.pricing{height:628px;text-align:center;padding-top:16px}
.plans{display:flex;gap:16px;width:952px;margin:26px auto 0}
.plan{width:307px;height:448px;background:var(--card);position:relative;padding:12px 10px 0}
.plan::after{content:"";position:absolute;right:0;bottom:0;width:34px;height:34px;background:var(--blue);clip-path:polygon(100% 0,100% 100%,0 100%)}
.plan-tag{font-size:11.5px;color:var(--muted)}
.price-box{background:var(--white);margin:12px 10px 0;height:116px;padding-top:12px;box-shadow:0 0 14px rgba(0,0,0,.08)}
.price{font-size:58px;font-weight:700;color:var(--blue);line-height:1}
.price sup{font-size:20px;vertical-align:14px;margin-right:2px}
.price-old{font-size:12px;color:var(--muted);text-decoration:line-through;margin-top:2px}
.price-note{font-size:10px;color:var(--muted);margin-top:4px;line-height:1.3}
.features{list-style:none;font-size:13px;color:var(--ink);margin-top:18px}
.features li{line-height:29px}
.plan .btn-row{justify-content:center;margin-top:16px;gap:0}
.plan .btn-yellow{width:124px;border-radius:3px 0 0 3px;padding:5px 0}
.plan .btn-dark{width:32px;height:29px;background:#2b2b2b;border-radius:0 3px 3px 0;display:flex;align-items:center;justify-content:center}
.btn-blue{display:inline-block;background:var(--blue);color:var(--white);font-size:15px;padding:7px 40px;border-radius:3px;margin-top:26px}

/* newsletter */
.newsletter{height:65px;background:linear-gradient(180deg,#2c2c2c,#1f1f1f);display:flex;align-items:center;padding-left:250px}
.newsletter h3{font-size:22px;font-weight:400;color:var(--white);width:238px}
.newsletter .field{width:344px;height:32px;background:#4a4a4a}
.newsletter .go{width:110px;height:32px;background:var(--yellow);font-size:14px;font-weight:700;color:var(--ink);text-align:center;line-height:32px}

/* partners */
.partners{height:146px;display:flex;align-items:center;justify-content:center;gap:44px}
.partners span{font-size:21px;font-weight:700;color:#555}

/* contact */
.contact{height:448px;position:relative}
.contact-photo{position:absolute;inset:0;background:linear-gradient(120deg,#1c1c1c 0%,#4a4038 30%,#2a2522 55%,#161616 100%)}
.contact-info{position:absolute;left:124px;top:34px;color:var(--white)}
.contact-info h2{font-size:36px;color:var(--yellow);font-weight:700}
.contact-list{list-style:none;margin-top:28px}
.contact-list li{display:flex;align-items:flex-start;gap:18px;font-size:15px;line-height:1.4;margin-bottom:30px}
.contact-list .ring{width:36px;height:36px;border-radius:50%;border:2px solid #888;display:flex;align-items:center;justify-content:center;flex:none}
.contact-list span{padding-top:8px}
.contact-form{position:absolute;left:500px;top:38px;width:576px;height:380px;background:rgba(40,40,40,.92);padding:26px 18px 0}
.input{height:48px;background:var(--white);border-radius:2px;font-size:11px;color:var(--muted);padding:16px 10px;margin-bottom:16px}
.input.tall{height:160px}
.contact-form .btn-row{gap:0}
.contact-form .btn-yellow{width:120px;text-align:center;border-radius:2px 0 0 2px;padding:6px 0}
.send-icon{width:32px;height:30px;background:#fff;display:flex;align-items:center;justify-content:center;border-radius:0 2px 2px 0}

/* footer */
.site-footer{height:27px;background:var(--blue);display:flex;align-items:center;justify-content:space-between;padding:0 124px;font-size:11px;color:var(--white)}
.site-footer nav{display:flex;gap:14px}
.site-footer nav a{color:var(--white);text-decoration:none}
.site-footer nav a:first-child{color:var(--yellow)}
</style>
</head>
<body>

<header class="site-header">
  <div class="brand"><div class="brand-mark"></div><div class="brand-name">TallyNest</div></div>
  <div class="top-contact">
    <span><i></i>info@tallynest-mail.co.uk</span>
    <span><i></i>0800-555-010-2468</span>
  </div>
  <nav class="nav">
    <a class="active" href="#">Home</a>
    <a href="#">Pricing</a>
    <a href="#">Updates</a>
    <a href="#">Blog</a>
    <a class="signup" href="#">Sign up</a>
    <a class="login" href="#">Login</a>
  </nav>
</header>

<section class="hero">
  <div class="hero-photo" role="img" aria-label="Photo of hands typing on a laptop keyboard"></div>
  <div class="hero-box">
    <h1 class="hero-title">Monitoring Your Website With <strong>TallyNest</strong></h1>
    <p class="hero-text">Lorem Ipsum is simply dummy text of the printing and typesetting industry. Lorem Ipsum has been the industry's standard dummy text ever since the 1500s, when an unknown printer took a galley of type and scrambled it to make a type specimen book. It has survived not only five centuries, but also the leap into electronic typesetting, remaining</p>
    <div class="btn-row">
      <span class="btn-yellow">Contact Us</span>
      <span class="btn-icon"><svg width="12" height="12" viewBox="0 0 12 12"><path d="M2 10 L9 3 M6 3 H9 V6" stroke="#fff" stroke-width="1.5" fill="none"/></svg></span>
    </div>
  </div>
  <div class="hero-notch"></div>
</section>

<section class="welcome">
  <h2 class="section-title">Welcom to TallyNest</h2>
  <p>Anyone with a website knows that things can sometimes go wrong. Sometimes it is with the code, the server or the network. TallyNest monitors your websites every minute and alerts you if your sites are down.</p>
  <p>A website can be down in various ways. It could be unreachable indicating a network problem, it could be up but throwing some sort of an error, or it could be mis-configured and not serving the correct content. Whatever the issue, TallyNest will identify it for you.</p>
</section>

<section class="services">
  <div class="services-photo" role="img" aria-label="Dark photo of a workspace behind the services"></div>
  <h2 class="section-title">TallyNest Services</h2>
  <div class="service-list">
    <article class="service-card">
      <div class="hex"><svg width="22" height="22" viewBox="0 0 22 22"><rect x="2" y="2" width="18" height="18" fill="none" stroke="#f2dc0a" stroke-width="2"/><path d="M4 12 H8 L10 7 L12 15 L14 11 H18" stroke="#f2dc0a" stroke-width="1.6" fill="none"/></svg></div>
      <h3>Monitoring</h3>
      <p>When your site is down it can mean lost sales,damageyo your brand, and lower search engine rankings. TallyNest has a global network of probe servers to test your website as often as every minute.</p>
      <div class="card-plus"><b></b><i>+</i><b></b></div>
    </article>
    <article class="service-card">
      <div class="hex"><svg width="22" height="22" viewBox="0 0 22 22"><path d="M11 3 C7 3 6 7 6 10 V14 L4 17 H18 L16 14 V10 C16 7 15 3 11 3 Z" fill="#f2dc0a"/><circle cx="11" cy="19" r="2" fill="#f2dc0a"/></svg></div>
      <h3>Alerting</h3>
      <p>When your site is down it can mean lost sales,damageyo your brand, and lower search engine rankings. TallyNest has a global network of probe servers to test your website as often as every minute.</p>
      <div class="card-plus"><b></b><i>+</i><b></b></div>
    </article>
    <article class="service-card">
      <div class="hex"><svg width="22" height="22" viewBox="0 0 22 22"><circle cx="7" cy="15" r="4" fill="none" stroke="#f2dc0a" stroke-width="2"/><circle cx="15" cy="15" r="4" fill="none" stroke="#f2dc0a" stroke-width="2"/><circle cx="11" cy="7" r="4" fill="none" stroke="#f2dc0a" stroke-width="2"/></svg></div>
      <h3>Stats</h3>
      <p>View performance trends in a beautifully designed UI. View uptime, downtime and the and a breakdown of response times to help diagnose where slowness is happening</p>
      <div class="card-plus"><b></b><i>+</i><b></b></div>
    </article>
    <article class="service-card">
      <div class="hex"><svg width="22" height="22" viewBox="0 0 22 22"><path d="M11 2 A9 9 0 1 0 20 11 H11 Z" fill="#f2dc0a"/><path d="M13 2 A8 8 0 0 1 20 9 H13 Z" fill="#f2dc0a"/></svg></div>
      <h3>API</h3>
      <p>When your site is down it can mean lost sales,damageyo your brand, and lower search engine rankings. TallyNest has a global network of probe servers to test your website as often as every minute.</p>
      <div class="card-plus"><b></b><i>+</i><b></b></div>
    </article>
  </div>
  <div class="dots"><i></i><i></i></div>
</section>

<section class="cta">
  <svg class="wave" width="1200" height="138" viewBox="0 0 1200 138" preserveAspectRatio="none"><path d="M0 40 Q600 -20 1200 40 V138 H0 Z" fill="#0a4fa6"/></svg>
  <div class="cta-inner">
    <div class="cta-copy">
      <h2>Start Now With TallyNest</h2>
      <p>Lorem Ipsum is simply dummy text of the printing and typesetting industry Lorem Ipsum has been the industry's standard dummy text ever since the 1500s, when an unknown printer took a galley of type</p>
    </div>
    <span class="cta-arrow"><svg width="16" height="16" viewBox="0 0 16 16"><path d="M5 2 L11 8 L5 14" stroke="#f2dc0a" stroke-width="2" fill="none"/></svg></span>
    <div class="cta-contact">
      <div>Phone : &nbsp;<b>0800-555-010-2468</b></div>
      <div>E-mail : &nbsp;<b>info@tallynest-mail.co.uk</b></div>
    </div>
  </div>
</section>

<section class="how">
  <div class="how-copy">
    <h2>How TallyNest Work</h2>
    <p>Lorem Ipsum is simply dummy text of the printing and typesetting industry. Lorem Ipsum has been the industry's standard dummy text ever since the 1500s, when an unknown printer took a galley of type and scrambled it to make a type specimen book. It has survived not only five centuries, but also the leap into electronic typesetting, remaining essentially unchanged. It was popularised in the 1960s with the release of Letraset sheets containing Lorem Ipsum passages,</p>
    <div class="btn-row">
      <span class="btn-yellow">Contact Us</span>
      <span class="btn-icon"><svg width="12" height="12" viewBox="0 0 12 12"><path d="M2 10 L9 3 M6 3 H9 V6" stroke="#fff" stroke-width="1.5" fill="none"/></svg></span>
    </div>
  </div>
  <div class="monitor" role="img" aria-label="Desktop monitor showing the dashboard with response time charts and a play button for the tour video"></div>
  <div class="how-rule"></div>
</section>

<section class="pricing">
  <h2 class="section-title">TallyNest Price Plan</h2>
  <div class="plans">
    <article class="plan">
      <div class="plan-tag">—— For Website and Server Monitoring ——</div>
      <div class="price-box"><div class="price">Free</div><div class="price-old">$10.00</div><div class="price-note">Lorem Ipsum is simply dummy text of the printing and<br>typesetting industry Lorem</div></div>
      <ul class="features"><li>Includes 10 Websites</li><li>1 min Poll Frequency</li><li>Includes 1 Advanced Monitor</li><li>100K RUM Pageviews</li><li>Select 8 Test Locations</li><li>50 SMS/Voice Credits Per Month</li><li>Standard Support</li></ul>
      <div class="btn-row"><span class="btn-yellow">Sign Up</span><span class="btn-dark"><svg width="8" height="10" viewBox="0 0 8 10"><path d="M2 1 L6 5 L2 9" stroke="#fff" stroke-width="1.6" fill="none"/></svg></span></div>
    </article>
    <article class="plan">
      <div class="plan-tag">—— For Website and Server Monitoring ——</div>
      <div class="price-box"><div class="price"><sup>$</sup>40.00</div><div class="price-old">$50.00</div><div class="price-note">Lorem Ipsum is simply dummy text of the printing and<br>typesetting industry Lorem</div></div>
      <ul class="features"><li>Includes 10 Websites</li><li>1 min Poll Frequency</li><li>Includes 1 Advanced Monitor</li><li>100K RUM Pageviews</li><li>Select 8 Test Locations</li><li>50 SMS/Voice Credits Per Month</li><li>Standard Support</li></ul>
      <div class="btn-row"><span class="btn-yellow">Sign Up</span><span class="btn-dark"><svg width="8" height="10" viewBox="0 0 8 10"><path d="M2 1 L6 5 L2 9" stroke="#fff" stroke-width="1.6" fill="none"/></svg></span></div>
    </article>
    <article class="plan">
      <div class="plan-tag">—— For Website and Server Monitoring ——</div>
      <div class="price-box"><div class="price"><sup>$</sup>80.00</div><div class="price-old">$100.00</div><div class="price-note">Lorem Ipsum is simply dummy text of the printing and<br>typesetting industry Lorem</div></div>
      <ul class="features"><li>Includes 10 Websites</li><li>1 min Poll Frequency</li><li>Includes 1 Advanced Monitor</li><li>100K RUM Pageviews</li><li>Select 8 Test Locations</li><li>50 SMS/Voice Credits Per Month</li><li>Standard Support</li></ul>
      <div class="btn-row"><span class="btn-yellow">Sign Up</span><span class="btn-dark"><svg width="8" height="10" viewBox="0 0 8 10"><path d="M2 1 L6 5 L2 9" stroke="#fff" stroke-width="1.6" fill="none"/></svg></span></div>
    </article>
  </div>
  <span class="btn-blue">View All Plans</span>
</section>

<section class="newsletter">
  <h3>Sign Up For Get Update:</h3>
  <div class="field"></div>
  <div class="go">Sign Up</div>
</section>

<section class="partners" aria-label="Clients">
  <span>Corvane</span><span>Halvery</span><span>Brakton</span><span>Quintora</span><span>Lunetta</span><span>Pellix</span><span>Strano</span>
</section>

<section class="contact">
  <div class="contact-photo" role="img" aria-label="Photo of a support agent wearing a headset"></div>
  <div class="contact-info">
    <h2>Get In Touch</h2>
    <ul class="contact-list">
      <li><span class="ring"><svg width="16" height="16" viewBox="0 0 16 16"><path d="M4 1 L6 5 L4.5 6.5 C5.5 8.5 7.5 10.5 9.5 11.5 L11 10 L15 12 L13.5 15 C7 14.5 1.5 9 1 2.5 Z" fill="#fff"/></svg></span><span>0800-555-010-2468</span></li>
      <li><span class="ring"><svg width="16" height="12" viewBox="0 0 16 12"><rect x="1" y="1" width="14" height="10" fill="#fff"/><path d="M1 1 L8 7 L15 1" stroke="#333" stroke-width="1.2" fill="none"/></svg></span><span>info@tallynest-mail.co.uk</span></li>
      <li><span class="ring"><svg width="14" height="18" viewBox="0 0 14 18"><path d="M7 1 C3.5 1 1 3.5 1 7 C1 11 7 17 7 17 C7 17 13 11 13 7 C13 3.5 10.5 1 7 1 Z" fill="#fff"/><circle cx="7" cy="7" r="2.2" fill="#333"/></svg></span><span>14 Fenwick Row, London,<br>United Kingdom.</span></li>
    </ul>
  </div>
  <form class="contact-form">
    <div class="input">NAME</div>
    <div class="input">EMAIL</div>
    <div class="input tall">MESSAGE</div>
    <div class="btn-row"><span class="btn-yellow">Send</span><span class="send-icon"><svg width="14" height="14" viewBox="0 0 14 14"><path d="M1 7 L13 1 L9 13 L7 8 Z" fill="#333"/></svg></span></div>
  </form>
</section>

<footer class="site-footer">
  <span>© 2016. All Rights Reserved.</span>
  <nav><a href="#">Home</a><a href="#">Pricing</a><a href="#">Updates</a><a href="#">Blog</a></nav>
</footer>

</body>
</html>
```